Website - freeride bike clothing company

Need a complete website with eCommerce.
Company: A new brand of bike (freeride) clothing...not the lycra stuff!

I have a design concept I have put together in Illustrator (see screen shots attached and below is a link to drop box with the full file - it was too heavy to attach here). The drop box folder also has images to use in the demo site. Refer to:
1) Landing Page - front page with images
2) Website - each subsequent page
3) Images folder
4) Logo for the website
https://www.filecrate-share.com/sh/k82pq7dm3xwa5/T9Lm4vQpzB

The above is my vision. Any design tips/suggestions to make it better are welcome. I want it to be easy to use and navigate and it needs to look RAD!

I do actually have a word press version of this with the first page already set up - if this can help?
I would like it up and running in 2 weeks (??), if possible.

I need to be able to turn on and off pages as I like, add products easily, team members etc.

I need eCommerce set up:
1) Direct to the public with pricing, shopping cart, online payment, shipping etc.
2) Wholesaler login. Same structure as public but I would need to pre-approve and set up any wholesalers to access this section, and it has different pricing.
I want to be able to turn on/off either of the above, ie: I might only use one or the other at one time.

Inspiration sites:
http://www.quellor.com/au/en/womens/
http://au.brindlefox.com/home.php
www.tarnvelomade.com

Site pages:
1) HOME - Landing Page

2) Gear
2a) Ladies / Mens / Other (each it's own page, same format, I can add new categories anytime)
2a(i) Item specific drill down

3) Crew
3a) Drill down per team member

4) Happenings
4a) News / Events
4b) Media
4c) Adventures
4d) Videos

5) Customer Service
5a) Policies / FAQ
5b) Size Chart
5c) Material
5d) Store Locator
5e) Contact

6) Shopping cart / check out and wholesaler login section

Target Market(s)

Extreme sports 25 - 40 year olds.
Men and women.
It is mostly a mens sport, but I am making womens gear too.

Industry/Entity Type

Clothing

Requirements
Must have
• Funky cool way to showcase my clothing products
Cool, simple yet professional look
Easily viewable photos of the product - easy to scroll between shots and to enlarge where needed.
Link to facebook and social media for the news sections, liking etc.
Crew section - link to that specific persons feed ie: on facebook/instagram

Pages:
1) Home Page

2) Gear
2a) Ladies / Mens / Other (same format pages - can add catagories as I like)
2ab) Item Specific Drill Down
2abc) Shopping Cart

3) Crew landing
3a) Crew Drill Down per person

4) Happenings
4a) News / Events / Media / Adventures / Videos

5) Customer Service
5a) Policies / FAQs
5ab) Size Chart
5abc) Material

6) Store Locator

7) Shopping Cart - both direct to public and a wholesale login section (I need to be able to grant people access and a login to the wholesale section)
Possibility to add promo codes to make things cheaper for specific people or sale time etc...

```html
<!DOCTYPE html>
<html lang="en">
<head>
<meta charset="utf-8">
<title>VARNOK</title>
<link href="https://fonts.googleapis.com/css2?family=Open+Sans:wght@400;600;700&display=swap" rel="stylesheet">
<style>
:root{
  --page:#f6f6f6;
  --ink:#333333;
  --ink-soft:#555555;
  --rule:#cfcfcf;
  --tile-dark:#000000;
  --white:#ffffff;
  --accent:#b5442a;
  --social:#6f7a8a;
}
*{margin:0;padding:0;box-sizing:border-box}
html,body{width:876px;height:1200px;overflow:hidden;background:var(--page)}
body{position:relative;font-family:"Open Sans",Arial,sans-serif;color:var(--ink)}
a{color:inherit;text-decoration:none}
.abs{position:absolute}

/* header */
.brand{left:126px;top:38px;display:flex;align-items:center;gap:8px}
.brand-mark{width:24px;height:24px;background:var(--ink);border-radius:50%}
.brand-name{font-size:23px;font-weight:700;letter-spacing:-0.5px;color:var(--ink);line-height:1}
.utility{right:125px;top:48px;font-size:7px;letter-spacing:1.3px;display:flex;gap:18px}
.header-rule{left:126px;top:83px;width:625px;height:1px;background:var(--rule)}
.main-nav{left:131px;top:98px;font-size:7.5px;letter-spacing:1.8px;display:flex}
.main-nav a{margin-right:56px}
.search{left:727px;top:92px;width:18px;height:18px;border-radius:50%;background:#222}

/* hero */
.hero{left:126px;top:122px;width:625px;height:297px;background:linear-gradient(180deg,#7fb0d8 0%,#cfe0ea 35%,#8a9a5a 55%,#cdbf9f 80%,#e2d7c0 100%)}
.hero-title{left:162px;top:340px;font-size:22px;letter-spacing:5px;color:#3a3a3a}
.hero-arrow{top:261px;width:30px;height:30px;background:var(--accent);opacity:.85}
.hero-arrow svg{width:30px;height:30px}

/* tiles */
.tile{width:203px;height:144px;overflow:hidden}
.tile-photo{display:flex;align-items:center;justify-content:center}
.tile-label{color:var(--white);font-size:15px;letter-spacing:4.5px;text-align:center;line-height:1.6;text-shadow:0 1px 2px rgba(0,0,0,.4)}
.tile-text{background:var(--tile-dark);color:var(--white);text-align:center;padding:20px 22px 0}
.tile-text h2{font-size:9.5px;font-weight:400;letter-spacing:2.5px;margin-bottom:12px}
.tile-text p{font-size:6px;line-height:11.2px;margin-bottom:11px}

.c1{left:126px}.c2{left:337px}.c3{left:548px}
.r1{top:434px}.r2{top:586px}.r3{top:738px}.r4{top:890px}

/* news */
.news-head{left:566px;top:746px;font-size:9px;letter-spacing:2.5px;font-weight:600}
.news-rule{left:564px;width:187px;height:1px;background:var(--rule)}
.news-item{left:565px;width:186px;display:flex;gap:12px}
.news-thumb{width:73px;height:60px;flex:none}
.news-body p{font-size:6px;line-height:11.2px;color:var(--ink-soft)}
.news-body .byline{font-size:6px;letter-spacing:1.3px;color:var(--ink);margin-top:4px;font-weight:600}

/* footer */
.footer-rule{left:126px;top:1062px;width:625px;height:2px;background:var(--rule)}
.foot-col{top:1078px}
.foot-col h3{font-size:8.5px;font-weight:600;letter-spacing:2.2px;margin-bottom:8px}
.foot-col li{list-style:none;font-size:6px;line-height:13.7px;padding-left:1px}
.social{display:flex;gap:7px;margin-top:3px}
.social span{width:19px;height:19px;border-radius:50%;background:var(--social);display:block}
.copyright{left:547px;top:1153px;font-size:6px}
</style>
</head>
<body>

<header>
  <a class="brand abs" href="#"><span class="brand-mark"></span><span class="brand-name">VARNOK</span></a>
  <nav class="utility abs"><a href="#">SHOP LOCATOR</a><span>|</span><a href="#">LOGIN</a><span>|</span><a href="#">SHOPPING CART</a></nav>
  <div class="header-rule abs"></div>
  <nav class="main-nav abs">
    <a href="#">HOME</a><a href="#">GEAR</a><a href="#">CREW</a><a href="#">HAPPENINGS</a><a href="#">CUSTOMER SERVICE</a>
  </nav>
  <div class="search abs"><svg width="18" height="18" viewBox="0 0 18 18"><circle cx="8" cy="8" r="3" fill="none" stroke="#fff" stroke-width="1.4"/><line x1="10.2" y1="10.2" x2="12.8" y2="12.8" stroke="#fff" stroke-width="1.6"/></svg></div>
</header>

<section>
  <div class="hero abs" role="img" aria-label="Downhill rider cornering on a dirt track under blue sky with race flags"></div>
  <div class="hero-title abs">GRAVITY</div>
  <a class="hero-arrow abs" style="left:126px" href="#"><svg viewBox="0 0 30 30"><polyline points="18,8 11,15 18,22" fill="none" stroke="#fff" stroke-width="1.2"/></svg></a>
  <a class="hero-arrow abs" style="left:721px" href="#"><svg viewBox="0 0 30 30"><polyline points="12,8 19,15 12,22" fill="none" stroke="#fff" stroke-width="1.2"/></svg></a>
</section>

<main>
  <article class="tile tile-text abs c1 r1">
    <h2>THE GEAR</h2>
    <p>Julien Arvel, riding for VARNOK, finished 21st in the Summit Rush - Open Challenger category!</p>
    <p>Julien was on the front line of the mass start on the glacier - with 350 people on his tail - not for the light hearted! An awesome result even with technical problems (a broken shifter)...</p>
  </article>
  <a class="tile tile-photo abs c2 r1" role="img" aria-label="Rider on a bicycle in an urban street" style="background:linear-gradient(160deg,#d9d9d6,#8a8580 60%,#4a4744)"><span class="tile-label" style="margin-top:40px">I LOVE<br>MY BICYCLE</span></a>
  <a class="tile tile-photo abs c3 r1" role="img" aria-label="Rider in helmet and colourful race jersey" style="background:linear-gradient(150deg,#c9c2b4,#c86a2c 45%,#3d6fb0 75%,#4a3a2a)"><span class="tile-label" style="margin-top:54px">MENS RANGE</span></a>

  <a class="tile tile-photo abs c1 r2" role="img" aria-label="Team rider speaking into a microphone at an event" style="background:linear-gradient(160deg,#8f9a7c,#4e5a48 50%,#6f6f68)"><span class="tile-label" style="margin-top:40px">JULIEN ARVEL</span></a>
  <a class="tile tile-photo abs c2 r2" role="img" aria-label="Pack of riders at a mass start on snow" style="background:linear-gradient(180deg,#a9bfd6,#9aa4ae 40%,#7b7f84)"><span class="tile-label" style="margin-top:54px">EVENTS</span></a>
  <a class="tile tile-photo abs c3 r2" role="img" aria-label="Woman standing with her mountain bike in the pit area" style="background:linear-gradient(180deg,#9db6d1,#7a7e7a 40%,#9b9b98)"><span class="tile-label" style="margin-top:54px">LADIES RANGE</span></a>

  <a class="tile tile-photo abs c1 r3" role="img" aria-label="Orange full-suspension bike frame close-up" style="background:linear-gradient(140deg,#3b5a32,#e58a1f 45%,#c46d1a 70%,#4a4030)"><span class="tile-label" style="margin-top:40px">RENNA COULTAS</span></a>
  <a class="tile tile-photo abs c2 r3" role="img" aria-label="Camera lens close-up" style="background:linear-gradient(120deg,#5b3a26,#c9a98a 50%,#2a2220)"><span class="tile-label" style="margin-top:56px">VIDEOS</span></a>

  <div class="news-head abs">NEWS</div>
  <div class="news-rule abs" style="top:765px"></div>
  <div class="news-item abs" style="top:780px">
    <div class="news-thumb" role="img" aria-label="Rider in jeans sitting on a skateboard" style="background:linear-gradient(180deg,#7d8b9c,#3f5678 60%,#b89a6a)"></div>
    <div class="news-body"><p>Julien was on the front line of the mass start on the glacier - with 350 people on his tail - not for the light hearted...</p><div class="byline">BY CORIN ADLEY</div></div>
  </div>
  <div class="news-rule abs" style="top:853px"></div>
  <div class="news-item abs" style="top:868px">
    <div class="news-thumb" role="img" aria-label="Rider descending a mountain trail" style="background:linear-gradient(180deg,#c9d3db,#8d9880 55%,#6b6650)"></div>
    <div class="news-body"><p>Julien was on the front line of the mass start on the glacier - with 350 people on his tail - not for the light hearted...</p><div class="byline">BY CORIN ADLEY</div></div>
  </div>
  <div class="news-rule abs" style="top:941px"></div>
  <div class="news-item abs" style="top:956px">
    <div class="news-thumb" role="img" aria-label="Red rally car at an event" style="background:linear-gradient(180deg,#6d7568,#c63a2e 55%,#5a5a5a)"></div>
    <div class="news-body"><p>Julien was on the front line of the mass start on the glacier - with 350 people on his tail - not for the light hearted...</p><div class="byline">BY CORIN ADLEY</div></div>
  </div>
  <div class="news-rule abs" style="top:1029px"></div>

  <article class="tile tile-text abs c1 r4">
    <h2>THE TEAM</h2>
    <p>Julien Arvel, riding for VARNOK, finished 21st in the Summit Rush - Open Challenger category!</p>
    <p>Julien was on the front line of the mass start on the glacier - with 350 people on his tail - not for the light hearted! An awesome result even with technical problems (a broken shifter)...</p>
  </article>
  <a class="tile tile-photo abs c2 r4" role="img" aria-label="Rider racing through a forest trail" style="background:linear-gradient(170deg,#4a5a32,#6b5a3a 50%,#3a2e22)"><span class="tile-label" style="margin-top:60px">OWEN BRACKLEY</span></a>
</main>

<footer>
  <div class="footer-rule abs"></div>
  <div class="foot-col abs" style="left:129px"><h3>GEAR</h3><ul><li>LADIES</li><li>MAN</li><li>GRAVITY</li><li>TRAIL</li></ul></div>
  <div class="foot-col abs" style="left:229px"><h3>CUSTOMER SERVICE</h3><ul><li>SIZE CHART</li><li>FABRIC DETAILS</li><li>POLICIES</li><li>CONTACT</li><li>FAQ</li></ul></div>
  <div class="foot-col abs" style="left:410px"><h3>HAPPENINGS</h3><ul><li>TEAM</li><li>EVENTS</li><li>ADVENTURES</li><li>MEDIA</li><li>VIDEOS</li></ul></div>
  <div class="foot-col abs" style="left:547px"><h3>SOCIALISE</h3><div class="social"><span></span><span></span><span></span><span></span></div></div>
  <div class="copyright abs">COPYRIGHT © 2013. VARNOK. ALL RIGHTS RESERVED.</div>
</footer>

</body>
</html>
```